Boilerplate Management Organization Chart

"Our Management Approach is a deliberate step-by-step process and supports our Technical Approach detailed in proposal submission. The Management Approach covers all the human capital aspects for executing a contract—from contract award through to sustainment and/or transition of the contract to another company. It includes how we organize, hire, staff, train, and account for our contract employees—as well as their complete personal life-cycle management within the company."

We need this management approach to depict an amazing management process that demonstrates best practices of the project management body of knowledge. We need this vector image to be applicable to any proposal without making references to any other proposals. Generic names but using strong business language.
Updates

Thanks for all designs submitted thus far. Some have stuck to the original type of chart. We would like to see a completely different way to show the same information. It has to be able to be recognized and deciphered very quickly by people who might not necessarily want to look at it. It must draw them in and make it incredibly easy to distinguish a management approach that looks fresh, infallible, and easily implemented.

Target Market(s)

Federal space, Government organizations looking for procedural efficiencies,

Industry/Entity Type

Management

Requirements
Must have
• Must not take up more than 1/3 to 1/2 of printable page and be clear.
Should not have
• Not too much color, but should stick to some color palette of some interest.

```html
<!DOCTYPE html>
<html lang="en">
<head>
<meta charset="utf-8">
<title>Management Approach – Process Chart</title>
<link rel="stylesheet" href="https://fonts.googleapis.com/css2?family=Montserrat:ital,wght@0,700;1,600&display=swap">
<style>
  :root {
    --canvas: #fefefc;
    --green-light: #cfdfb7;
    --green-dark: #adbf8e;
    --blue-light: #c8e6f6;
    --blue-dark: #8fcbeb;
    --heading-grey: #5f6062;
    --arrow-grey: #5b5c5e;
    --label-ink: #1b1b1b;
  }
  * { margin: 0; padding: 0; box-sizing: border-box; }
  html, body { width: 1200px; height: 1000px; overflow: hidden; background: var(--canvas); }
  .chart { position: relative; width: 1200px; height: 1000px; font-family: "Montserrat", Arial, sans-serif; }

  .phase-band { position: absolute; left: 0; top: 0; }
  .phase-title {
    position: absolute;
    font-style: italic; font-weight: 600; font-size: 33px; letter-spacing: 0.5px;
    color: var(--heading-grey); white-space: nowrap; line-height: 1;
  }
  .phase-title--management { left: 172px; top: 190px; }
  .phase-title--evaluation { right: 175px; top: 782px; }

  .step { position: absolute; width: 200px; height: 200px; }
  .step svg { position: absolute; inset: 0; overflow: visible; }
  .step-label {
    position: absolute; inset: 0;
    display: flex; align-items: center; justify-content: center; text-align: center;
    font-weight: 700; font-size: 16px; line-height: 1.4; color: var(--label-ink); text-transform: uppercase;
  }
  .step--green .disc { fill: var(--green-light); }
  .step--green .ring { stroke: var(--green-dark); }
  .step--blue .disc { fill: var(--blue-light); }
  .step--blue .ring { stroke: var(--blue-dark); }
  .ring { fill: none; stroke-width: 14; }

  .connector { position: absolute; left: 0; top: 0; }
  .connector--green { fill: var(--green-dark); }
  .connector--blue { fill: var(--blue-dark); }
  .connector--turn { fill: var(--arrow-grey); }
</style>
</head>
<body>
<main class="chart" aria-label="Management approach process chart">

  <svg class="phase-band" width="1200" height="1000" aria-hidden="true">
    <polygon points="163,130 1035,222 163,222" fill="var(--green-light)"/>
    <rect x="163" y="222" width="872" height="14" fill="var(--green-dark)"/>
    <rect x="165" y="763" width="872" height="14" fill="var(--blue-dark)"/>
    <polygon points="165,777 1037,777 1037,868" fill="var(--blue-light)"/>
  </svg>

  <h1 class="phase-title phase-title--management">MANAGEMENT APPROACH</h1>
  <h2 class="phase-title phase-title--evaluation">PROGRAM EVALUATION</h2>

  <!-- Process connectors -->
  <svg class="connector" width="1200" height="1000" aria-hidden="true">
    <g class="connector--green">
      <polygon points="348,345 383,370 348,395"/>
      <polygon points="582,345 617,370 582,395"/>
      <polygon points="816,345 851,370 816,395"/>
    </g>
    <polygon class="connector--turn" points="926,483 984,483 955,517"/>
    <g class="connector--blue">
      <polygon points="852,615 817,640 852,665"/>
      <polygon points="618,615 583,640 618,665"/>
      <polygon points="384,615 349,640 384,665"/>
    </g>
  </svg>

  <!-- Management approach row -->
  <div class="step step--green" style="left:155px; top:268px;">
    <svg width="200" height="200" aria-hidden="true"><circle class="disc" cx="100" cy="100" r="85"/><path class="ring" d="M177.9,145 A90,90 0 1 1 26.3,48.4"/></svg>
    <p class="step-label">Responsability<br>Fixed</p>
  </div>
  <div class="step step--green" style="left:388px; top:268px;">
    <svg width="200" height="200" aria-hidden="true"><circle class="disc" cx="100" cy="100" r="85"/><path class="ring" d="M26.3,151.6 A90,90 0 1 1 177.9,55"/></svg>
    <p class="step-label">Management<br>&amp;<br>Oversight</p>
  </div>
  <div class="step step--green" style="left:622px; top:268px;">
    <svg width="200" height="200" aria-hidden="true"><circle class="disc" cx="100" cy="100" r="85"/><path class="ring" d="M177.9,145 A90,90 0 1 1 26.3,48.4"/></svg>
    <p class="step-label">Manning<br>the Team</p>
  </div>
  <div class="step step--green" style="left:855px; top:268px;">
    <svg width="200" height="200" aria-hidden="true"><circle class="disc" cx="100" cy="100" r="85"/><path class="ring" d="M26.3,151.6 A90,90 0 1 1 177.9,55"/></svg>
    <p class="step-label">Training</p>
  </div>

  <!-- Program evaluation row -->
  <div class="step step--blue" style="left:855px; top:538px;">
    <svg width="200" height="200" aria-hidden="true"><circle class="disc" cx="100" cy="100" r="85"/><path class="ring" d="M22.1,55 A90,90 0 1 1 145,177.9"/></svg>
    <p class="step-label">Professional<br>Development</p>
  </div>
  <div class="step step--blue" style="left:622px; top:538px;">
    <svg width="200" height="200" aria-hidden="true"><circle class="disc" cx="100" cy="100" r="85"/><path class="ring" d="M145,22.1 A90,90 0 1 1 22.1,145"/></svg>
    <p class="step-label">Retention /<br>Quality of Life</p>
  </div>
  <div class="step step--blue" style="left:388px; top:538px;">
    <svg width="200" height="200" aria-hidden="true"><circle class="disc" cx="100" cy="100" r="85"/><path class="ring" d="M22.1,145 A90,90 0 1 1 177.9,145"/></svg>
    <p class="step-label">Benefits</p>
  </div>
  <div class="step step--blue" style="left:155px; top:538px;">
    <svg width="200" height="200" aria-hidden="true"><circle class="disc" cx="100" cy="100" r="85"/><path class="ring" d="M145,22.1 A90,90 0 1 1 22.1,145"/></svg>
    <p class="step-label">Sustainment /<br>Transition</p>
  </div>

</main>
</body>
</html>
```